Corvane spray foam and Environmental

I have business cards but need new ones. The ones I have are very bland. Here is. Y company website http://www.corvanesprayfoam.ca

Also I can send you copies of the current cards
I would also need my current logo on the new design as well.. Also spray foam and Environmental

Industry/Entity Type

Business

Logo Text

Corvane.

```html
<!DOCTYPE html>
<html lang="en">
<head>
<meta charset="utf-8">
<title>Corvane Business Cards</title>
<link href="https://fonts.googleapis.com/css2?family=Lato:wght@400;700;900&display=swap" rel="stylesheet">
<style>
  :root {
    --purple: #6a3d8a;
    --green: #4cc81e;
    --grey: #a3a3a3;
    --ink: #1f1f1f;
    --paper: #ffffff;
    --backdrop: #d9d9db;
  }
  * { box-sizing: border-box; margin: 0; padding: 0; }
  html, body { width: 1200px; height: 1059px; overflow: hidden; }
  body {
    background: var(--backdrop);
    font-family: "Lato", sans-serif;
    color: var(--ink);
    position: relative;
  }
  .card {
    position: absolute;
    left: 180px;
    width: 840px;
    height: 480px;
    background: var(--paper);
    box-shadow: 0 6px 18px rgba(0,0,0,0.18);
    overflow: hidden;
  }
  .card--services { top: 33px; }
  .card--contact { top: 546px; }

  .brand { position: absolute; left: 90px; top: 95px; display: flex; align-items: center; }
  .brand__mark {
    width: 160px; height: 115px;
    border-radius: 18px;
    background: var(--purple);
  }
  .brand__name {
    margin-left: 36px;
    font-weight: 900;
    font-size: 96px;
    letter-spacing: 6px;
    color: var(--purple);
    line-height: 1;
  }

  .division-title {
    font-weight: 700;
    font-size: 24px;
    letter-spacing: 1px;
    text-transform: uppercase;
    margin-bottom: 8px;
  }
  .division-title--foam { color: var(--purple); }
  .division-title--env { color: var(--green); }

  .service-list { list-style: none; }
  .service-list li {
    font-size: 19px;
    text-transform: uppercase;
    letter-spacing: 0.5px;
    line-height: 25px;
    padding-left: 18px;
    position: relative;
  }
  .service-list li::before {
    content: "";
    position: absolute; left: 2px; top: 10px;
    width: 7px; height: 7px; border-radius: 50%;
  }
  .service-list--foam li::before { background: var(--purple); }
  .service-list--env li::before { background: var(--green); }

  .services--env { position: absolute; left: 480px; top: 240px; }
  .services--foam { position: absolute; left: 90px; top: 265px; }

  .contact-block { position: absolute; z-index: 1; }
  .contact-block--foam { left: 100px; top: 262px; }
  .contact-block--env { left: 490px; top: 228px; }
  .contact-list { list-style: none; }
  .contact-list li {
    display: flex; align-items: center;
    font-size: 20px;
    line-height: 30px;
  }
  .contact-list svg { width: 16px; height: 16px; margin-right: 14px; flex: none; }
  .contact-list--foam svg { fill: var(--purple); stroke: var(--purple); }
  .contact-list--env svg { fill: var(--green); stroke: var(--green); }

  .divider {
    position: absolute; left: 455px; top: 240px;
    width: 1px; height: 110px;
    background: var(--purple);
  }
  .wave { position: absolute; left: 0; top: 0; width: 840px; height: 480px; }
</style>
</head>
<body>

<section class="card card--services">
  <div class="brand">
    <div class="brand__mark"></div>
    <div class="brand__name">CORVANE</div>
  </div>

  <div class="services--env">
    <h3 class="division-title division-title--env">Environmantal</h3>
    <ul class="service-list service-list--env">
      <li>Air Monitoring</li>
      <li>Asbestos Testing</li>
      <li>Asbestos Removal</li>
      <li>Building Demolition</li>
      <li>Lead Testing</li>
      <li>Mould Removal</li>
    </ul>
  </div>

  <div class="services--foam">
    <h3 class="division-title division-title--foam">Spray Foam</h3>
    <ul class="service-list service-list--foam">
      <li>Roofing Foam</li>
      <li>Slabjacking</li>
      <li>2 Pound / Half Pound</li>
      <li>Sound Proofing</li>
      <li>Batt Insulation</li>
      <li>Attic Blow In</li>
    </ul>
  </div>
</section>

<section class="card card--contact">
  <svg class="wave" viewBox="0 0 840 480" aria-hidden="true">
    <path d="M0,442 C320,432 600,420 720,402 S825,380 840,372" fill="none" stroke="#a3a3a3" stroke-width="9"/>
    <path d="M0,458 C340,448 620,434 740,416 S830,394 840,388 L840,480 L0,480 Z" fill="#6a3d8a"/>
  </svg>

  <div class="brand">
    <div class="brand__mark"></div>
    <div class="brand__name">CORVANE</div>
  </div>

  <div class="contact-block contact-block--foam">
    <h3 class="division-title division-title--foam">Spray Foam</h3>
    <ul class="contact-list contact-list--foam">
      <li><svg viewBox="0 0 16 16"><path d="M3 1 L6 1 L7 5 L5 6.5 C6 9 7 10 9.5 11 L11 9 L15 10 L15 13 C15 14 14 15 13 15 C6 15 1 10 1 3 C1 2 2 1 3 1 Z" stroke="none"/></svg>604-555-0148</li>
      <li><svg viewBox="0 0 16 16"><rect x="1" y="3" width="14" height="10" stroke="none"/><path d="M1.5 3.5 L8 9 L14.5 3.5" fill="none" stroke="#fff" stroke-width="1.4"/></svg>corvanefoam@gmail.com</li>
      <li><svg viewBox="0 0 16 16"><circle cx="8" cy="8" r="6.5" fill="none" stroke-width="1.6"/><path d="M1.5 8 H14.5 M8 1.5 V14.5 M3 4.5 H13 M3 11.5 H13" fill="none" stroke-width="1.2"/></svg>www.corvanefoam.com</li>
    </ul>
  </div>

  <div class="divider"></div>

  <div class="contact-block contact-block--env">
    <h3 class="division-title division-title--env">Environmental</h3>
    <ul class="contact-list contact-list--env">
      <li><svg viewBox="0 0 16 16"><path d="M3 1 L6 1 L7 5 L5 6.5 C6 9 7 10 9.5 11 L11 9 L15 10 L15 13 C15 14 14 15 13 15 C6 15 1 10 1 3 C1 2 2 1 3 1 Z" stroke="none"/></svg>604-555-0193</li>
      <li><svg viewBox="0 0 16 16"><rect x="1" y="3" width="14" height="10" stroke="none"/><path d="M1.5 3.5 L8 9 L14.5 3.5" fill="none" stroke="#fff" stroke-width="1.4"/></svg>corvaneenviromental@gmail.com</li>
      <li><svg viewBox="0 0 16 16"><circle cx="8" cy="8" r="6.5" fill="none" stroke-width="1.6"/><path d="M1.5 8 H14.5 M8 1.5 V14.5 M3 4.5 H13 M3 11.5 H13" fill="none" stroke-width="1.2"/></svg>www.corvaneenviromental.com</li>
    </ul>
  </div>
</section>

</body>
</html>
```